Book about Ice Dragons

I would like a book cover made for my book i am planning on releasing soon, the book is title "Corvath: DUSK", i would like a white background with the words Corvath: DUSK in the middle with some sort of dragon medallion / logo in the middle, i would love the wording to have a subtle ice effect, on the back i want a small picture at the top with a a dragon perched on a rock with a man standing below the dragon, I want the dragon to dwarf the man, I like the stronger dinosaur like dragons not the Chinese style. I really like the way the dragon looks in the attached picture but i'm not a fan of the whiskers on the dragons face.

```html
<!DOCTYPE html>
<html lang="en">
<head>
<meta charset="utf-8">
<title>Corvath: DUSK — Book Cover</title>
<link rel="stylesheet" href="https://fonts.googleapis.com/css2?family=Bebas+Neue&family=Oswald:wght@500;600&display=swap">
<style>
  :root {
    --frost-white: #f7fafc;
    --frost-mist: #e2ecf1;
    --frost-shadow: #c9d9e2;
    --spine-tone: #dbe6ec;
    --spine-edge: #b9cdd8;
    --ice-blue: #5aa2cf;
    --ice-light: #a6d2ea;
    --ice-deep: #3b80b0;
    --author-blue: #5f98bf;
    --medal-light: #ece0c2;
    --medal-mid: #cdb487;
    --medal-dark: #8f7650;
  }
  html, body {
    margin: 0;
    padding: 0;
    width: 870px;
    height: 1200px;
    overflow: hidden;
    background: #ffffff;
  }
  .book-jacket {
    position: relative;
    width: 870px;
    height: 1200px;
    overflow: hidden;
    display: flex;
  }
  .frost-texture {
    position: absolute;
    inset: 0;
    width: 870px;
    height: 1200px;
    pointer-events: none;
  }

  /* Spine */
  .spine {
    position: relative;
    width: 130px;
    height: 1200px;
    background: linear-gradient(90deg, var(--spine-edge) 0%, var(--spine-tone) 30%, var(--frost-mist) 75%, var(--spine-edge) 100%);
    display: flex;
    flex-direction: column;
    align-items: center;
    box-sizing: border-box;
    padding: 70px 0 60px;
  }
  .spine__author {
    writing-mode: vertical-rl;
    font-family: "Oswald", sans-serif;
    font-weight: 600;
    font-size: 44px;
    letter-spacing: 0.08em;
    color: var(--ice-deep);
    margin: 0;
  }
  .spine__imprint {
    margin-top: 36px;
    display: flex;
    flex-direction: column;
    align-items: center;
    gap: 10px;
  }
  .spine__imprint-dot {
    width: 34px;
    height: 34px;
    border-radius: 50%;
    background: var(--ice-deep);
  }
  .spine__imprint-name {
    writing-mode: vertical-rl;
    font-family: "Oswald", sans-serif;
    font-weight: 500;
    font-size: 18px;
    letter-spacing: 0.12em;
    color: var(--ice-deep);
  }
  .spine__title {
    margin-top: auto;
    width: 100px;
    height: 560px;
  }

  /* Front cover */
  .front-cover {
    position: relative;
    width: 740px;
    height: 1200px;
    background:
      radial-gradient(ellipse at 30% 20%, rgba(255,255,255,0.9) 0%, rgba(255,255,255,0) 55%),
      radial-gradient(ellipse at 75% 70%, rgba(198,214,223,0.55) 0%, rgba(198,214,223,0) 60%),
      linear-gradient(160deg, var(--frost-white) 0%, var(--frost-mist) 55%, var(--frost-shadow) 100%);
    box-shadow: inset 8px 0 14px rgba(120,150,170,0.25);
  }
  .front-cover__title {
    position: absolute;
    top: 60px;
    left: 0;
    width: 740px;
    height: 460px;
  }
  .title-text {
    font-family: "Bebas Neue", "Oswald", sans-serif;
  }
  .medallion {
    position: absolute;
    left: 235px;
    top: 600px;
    width: 270px;
    height: 380px;
    transform: rotate(-8deg);
  }
  .medallion__loop {
    position: absolute;
    left: 50%;
    top: 0;
    transform: translateX(-50%);
    width: 50px;
    height: 50px;
    border-radius: 50%;
    border: 7px solid var(--medal-mid);
    box-sizing: border-box;
  }
  .medallion__disc {
    position: absolute;
    left: 0;
    top: 44px;
    width: 270px;
    height: 330px;
    border-radius: 50%;
    background: radial-gradient(ellipse at 40% 35%, var(--medal-light) 0%, var(--medal-mid) 62%, var(--medal-dark) 100%);
    box-shadow: 0 14px 26px rgba(90,110,125,0.25);
  }
  .front-cover__author {
    position: absolute;
    bottom: 70px;
    left: 0;
    width: 740px;
    margin: 0;
    text-align: center;
    font-family: "Oswald", sans-serif;
    font-weight: 600;
    font-size: 46px;
    letter-spacing: 0.06em;
    text-transform: uppercase;
    color: var(--author-blue);
  }
</style>
</head>
<body>
  <div class="book-jacket">
    <svg width="0" height="0" style="position:absolute">
      <defs>
        <linearGradient id="ice-fill" x1="0" y1="0" x2="0" y2="1">
          <stop offset="0" stop-color="#a6d2ea"/>
          <stop offset="0.5" stop-color="#5aa2cf"/>
          <stop offset="1" stop-color="#3b80b0"/>
        </linearGradient>
        <filter id="ice-texture" x="-5%" y="-5%" width="110%" height="110%">
          <feTurbulence type="fractalNoise" baseFrequency="0.035 0.09" numOctaves="4" seed="7" result="noise"/>
          <feDisplacementMap in="SourceGraphic" in2="noise" scale="5" result="rough"/>
          <feColorMatrix in="noise" type="matrix" values="0 0 0 0 1  0 0 0 0 1  0 0 0 0 1  0 0 0 2.4 -1.2" result="frost"/>
          <feComposite in="frost" in2="rough" operator="in" result="frostOnText"/>
          <feMerge>
            <feMergeNode in="rough"/>
            <feMergeNode in="frostOnText"/>
          </feMerge>
        </filter>
      </defs>
    </svg>

    <aside class="spine">
      <p class="spine__author">ELIAS MARROW</p>
      <div class="spine__imprint">
        <span class="spine__imprint-dot"></span>
        <span class="spine__imprint-name">NORTHVALE</span>
      </div>
      <svg class="spine__title" viewBox="0 0 100 560" aria-label="Corvath: DUSK">
        <text class="title-text" x="0" y="0" transform="translate(28 10) rotate(90)" font-size="86" letter-spacing="4" fill="url(#ice-fill)" filter="url(#ice-texture)">CORVATH: DUSK</text>
      </svg>
    </aside>

    <main class="front-cover">
      <svg class="front-cover__title" viewBox="0 0 740 460" aria-label="Corvath: DUSK">
        <text class="title-text" x="370" y="195" text-anchor="middle" font-size="200" letter-spacing="10" fill="url(#ice-fill)" filter="url(#ice-texture)">CORVATH:</text>
        <text class="title-text" x="370" y="400" text-anchor="middle" font-size="200" letter-spacing="16" fill="url(#ice-fill)" filter="url(#ice-texture)">DUSK</text>
      </svg>
      <div class="medallion" role="img" aria-label="Bronze pendant medallion engraved with a dragon emblem">
        <div class="medallion__loop"></div>
        <div class="medallion__disc"></div>
      </div>
      <p class="front-cover__author">Elias Marrow</p>
    </main>

    <svg class="frost-texture" viewBox="0 0 870 1200" aria-hidden="true">
      <filter id="frost-grain">
        <feTurbulence type="fractalNoise" baseFrequency="0.012 0.03" numOctaves="4" seed="3"/>
        <feColorMatrix type="matrix" values="0 0 0 0 1  0 0 0 0 1  0 0 0 0 1  0 0 0 1.1 -0.45"/>
      </filter>
      <rect width="870" height="1200" filter="url(#frost-grain)" opacity="0.55"/>
    </svg>
  </div>
</body>
</html>
```